Envelope Design - Winner can do follow-up business

- Varindo.com is a Swiss-based online store selling business shirts and accessories for business men
- Please visit the webpage to make yourself familiar with the company. Although the text is in German, with Google translator you should be able to understand the main content.
- Our clients are mainly business men between 30 and 60 years old. Mostly with a high income working in the service industry (banking, insurance, lawyers, etc.). Sometimes there wives purchase the shirts for them ;-)
- The colors and the logo are given, as they are also used for the print materials (please see files in attachment)
- I am running several businesses and often need a talented web designer --> the winner gets substantial follow-up business
your task:
-for our company we need a new envelope design
-It should be simple and modern
-please use one of the logos in the followings.
-suprise me :)

```html
<!DOCTYPE html>
<html lang="de">
<head>
<meta charset="utf-8">
<title>Varindo – Briefumschlag</title>
<link href="https://fonts.googleapis.com/css2?family=Montserrat:wght@400;500;600&display=swap" rel="stylesheet">
<style>
  :root {
    --page-bg: #ececec;
    --paper: #f7f7f7;
    --facet-light: #f4f4f4;
    --facet-mid: #e4e4e4;
    --facet-dark: #d6d6d6;
    --brand-gold: #c9b23a;
    --brand-red: #c8303a;
    --ink: #6f6f6f;
    --ink-strong: #333333;
  }
  html, body {
    margin: 0;
    padding: 0;
    width: 1200px;
    height: 900px;
    overflow: hidden;
    background: var(--page-bg);
  }
  .canvas {
    position: relative;
    width: 1200px;
    height: 900px;
  }
  .envelope {
    position: absolute;
    left: 80px;
    top: 190px;
    width: 1040px;
    height: 520px;
    background: var(--paper);
    box-shadow: 0 10px 30px rgba(0,0,0,0.10), 0 2px 4px rgba(0,0,0,0.06);
    overflow: hidden;
  }
  .envelope__pattern {
    position: absolute;
    inset: 0;
    background:
      linear-gradient(135deg, var(--facet-mid) 0%, var(--facet-light) 30%, var(--facet-dark) 55%, var(--facet-light) 75%, var(--facet-mid) 100%);
    opacity: 0.85;
  }
  .brand {
    position: absolute;
    right: 70px;
    top: 170px;
    display: flex;
    align-items: center;
    gap: 16px;
  }
  .brand__mark {
    width: 22px;
    height: 22px;
    background: var(--brand-red);
  }
  .brand__name {
    font-family: "Montserrat", sans-serif;
    font-weight: 500;
    font-size: 58px;
    letter-spacing: 10px;
    color: var(--brand-gold);
    line-height: 1;
  }
  .sender {
    position: absolute;
    right: 70px;
    bottom: 70px;
    text-align: right;
    font-family: "Montserrat", sans-serif;
    font-size: 19px;
    line-height: 1.45;
    color: var(--ink);
  }
  .sender p { margin: 0; }
  .sender__web {
    margin-top: 12px !important;
    font-weight: 600;
    color: var(--ink-strong);
  }
</style>
</head>
<body>
  <main class="canvas">
    <section class="envelope">
      <div class="envelope__pattern" role="img" aria-label="Faint grey low-poly faceted background pattern"></div>
      <div class="brand">
        <span class="brand__mark"></span>
        <span class="brand__name">VARINDO</span>
      </div>
      <address class="sender">
        <p>Hauptsitz/Postadresse:</p>
        <p>Varindo GmbH | Seeblickweg 21</p>
        <p>8805 Richterswil</p>
        <p class="sender__web">www.varindo.com</p>
      </address>
    </section>
  </main>
</body>
</html>
```